Business Card design for a company called Tallow Flame NI

I need a business card design for my oil fired boiler servicing company. I have a logo design already and Im just looking that incorporated into the business card design. card details; Tallow Flame NI
Oil Burner Servicing - Mid Ulster Area
Service Engineer - Owen Marsh
Mobile 07751364927
email - Tallow.Flame.NI@hearthmail.example
www.tallowflameni.example
I carry out Servicing, Commissioning, Fault Finding, Warranty Validation
Target Market(s)
home owners with oil fired central heating
Industry/Entity Type
Business
Contact Information for Business Card
Tallow Flame NI
Tell. 07751364927
Web: www.tallowflameni.example
email Tallow.Flame.NI@Hearthmail.Example
Servicing Fault Finding Commissioning Warranty Validation
Look and feel

```html
<!DOCTYPE html>
<html lang="en">
<head>
<meta charset="utf-8">
<title>Tallow Flame NI – Business Cards</title>
<link href="https://fonts.googleapis.com/css2?family=Roboto:wght@300;400;500&family=Roboto+Condensed:wght@400&display=swap" rel="stylesheet">
<style>
  :root {
    --backdrop: #cbb08a;
    --card-black: #000000;
    --lime: #d6e02a;
    --leaf: #8cc63f;
    --brand-green: #6cc04a;
    --ink: #111111;
    --paper: #ffffff;
  }
  html, body {
    margin: 0;
    padding: 0;
    overflow: hidden;
  }
  body {
    width: 800px;
    height: 1200px;
    background: var(--backdrop);
    position: relative;
  }
  .card {
    position: absolute;
    left: 137px;
    width: 535px;
    height: 298px;
    display: block;
  }
  .card--front-green { top: 126px; }
  .card--back-black { top: 437px; }
  .card--centered-black { top: 748px; }

  .brand-name {
    font-family: "Roboto", Arial, sans-serif;
    font-weight: 500;
    font-size: 22px;
    fill: var(--brand-green);
  }
  .brand-tagline {
    font-family: "Roboto", Arial, sans-serif;
    font-weight: 400;
    font-size: 6.4px;
    letter-spacing: 0.9px;
    fill: var(--brand-green);
  }
  .brand-dot { fill: var(--brand-green); }
  .person-name {
    font-family: "Roboto", Arial, sans-serif;
    font-weight: 300;
    font-size: 30px;
  }
  .person-role {
    font-family: "Roboto", Arial, sans-serif;
    font-weight: 300;
    font-size: 15px;
  }
  .contact {
    font-family: "Roboto Condensed", "Arial Narrow", sans-serif;
    font-size: 13px;
  }
  .contact--email { font-size: 12px; }
  .on-green { fill: var(--ink); }
  .on-black { fill: var(--paper); }
  .icon-ink { fill: var(--ink); stroke: var(--ink); }
  .icon-paper { fill: var(--paper); stroke: var(--paper); }
  .divider { stroke: var(--paper); stroke-width: 1.6; }
</style>
</head>
<body>

<svg width="0" height="0" style="position:absolute" aria-hidden="true">
  <defs>
    <linearGradient id="limeSweep" x1="0" x2="1" y1="0" y2="0">
      <stop offset="0" stop-color="#d6e02a"/>
      <stop offset="1" stop-color="#8cc63f"/>
    </linearGradient>
    <symbol id="icon-pin" viewBox="0 0 12 12">
      <path d="M6 0.5a3.8 3.8 0 0 0-3.8 3.8C2.2 7 6 11.5 6 11.5S9.8 7 9.8 4.3A3.8 3.8 0 0 0 6 0.5zm0 5.3a1.5 1.5 0 1 1 0-3 1.5 1.5 0 0 1 0 3z" stroke="none"/>
    </symbol>
    <symbol id="icon-phone" viewBox="0 0 12 12">
      <path d="M3.2 1l1.6 0 .6 2.2-1 .8c.5 1.6 1.4 3 2.6 4l1-.7 2 1.1-.3 1.6c-.2.5-.7.8-1.2.7C5 10 2.2 6.4 2.3 2.3c0-.7.4-1.2.9-1.3z" stroke="none"/>
    </symbol>
    <symbol id="icon-at" viewBox="0 0 12 12">
      <circle cx="6" cy="6" r="2" fill="none" stroke-width="1.3"/>
      <path d="M8 4v2.8c0 .9 1.8 1 2-.3.5-3-1.5-5-4-5a4.6 4.6 0 1 0 2.6 8.4" fill="none" stroke-width="1.3"/>
    </symbol>
    <symbol id="icon-globe" viewBox="0 0 12 12">
      <g fill="none" stroke-width="1">
        <circle cx="6" cy="6" r="5"/>
        <ellipse cx="6" cy="6" rx="2.2" ry="5"/>
        <line x1="1" y1="6" x2="11" y2="6"/>
        <line x1="2" y1="3.5" x2="10" y2="3.5"/>
        <line x1="2" y1="8.5" x2="10" y2="8.5"/>
      </g>
    </symbol>
  </defs>
</svg>

<!-- Front card, lime gradient -->
<svg class="card card--front-green" viewBox="0 0 535 298" role="group" aria-label="Tallow Flame NI business card, green front">
  <rect width="535" height="298" fill="url(#limeSweep)"/>
  <path class="brand-band" d="M0 57 H250 a41.5 41.5 0 0 1 0 83 H0 Z" fill="var(--card-black)"/>
  <circle class="brand-dot" cx="56" cy="99" r="24"/>
  <text class="brand-name" x="90" y="103">Tallow Flame NI</text>
  <text class="brand-tagline" x="90" y="115">OIL BURNER SERVICING - MID ULSTER AREA</text>

  <text class="person-name on-green" x="80" y="221">Owen Marsh</text>
  <text class="person-role on-green" x="81" y="243">Service Engineer</text>

  <use href="#icon-pin" class="icon-ink" x="305" y="178" width="12" height="12"/>
  <text class="contact on-green" x="326" y="189">#00 Adress 01, Adress, City</text>
  <use href="#icon-phone" class="icon-ink" x="305" y="201" width="12" height="12"/>
  <text class="contact on-green" x="326" y="212">077 51 364 927</text>
  <use href="#icon-at" class="icon-ink" x="305" y="224" width="12" height="12"/>
  <text class="contact contact--email on-green" x="326" y="235">tallow.flame.ni@hearthmail.example</text>
  <use href="#icon-globe" class="icon-ink" x="305" y="248" width="12" height="12"/>
  <text class="contact on-green" x="326" y="258">www.tallowflameni.example</text>
</svg>

<!-- Back card, black with divider -->
<svg class="card card--back-black" viewBox="0 0 535 298" role="group" aria-label="Tallow Flame NI business card, black back">
  <rect width="535" height="298" fill="var(--card-black)"/>
  <circle class="brand-dot" cx="56" cy="86" r="24"/>
  <text class="brand-name" x="90" y="91">Tallow Flame NI</text>
  <text class="brand-tagline" x="90" y="102">OIL BURNER SERVICING - MID ULSTER AREA</text>

  <text class="person-name on-black" x="80" y="220">Owen Marsh</text>
  <text class="person-role on-black" x="81" y="241">Service Engineer</text>

  <line class="divider" x1="268" y1="156" x2="268" y2="273"/>

  <use href="#icon-pin" class="icon-paper" x="311" y="177" width="12" height="12"/>
  <text class="contact on-black" x="338" y="188">#00 Adress 01, Adress, City</text>
  <use href="#icon-phone" class="icon-paper" x="311" y="201" width="12" height="12"/>
  <text class="contact on-black" x="338" y="212">077 51 364 927</text>
  <use href="#icon-at" class="icon-paper" x="311" y="226" width="12" height="12"/>
  <text class="contact contact--email on-black" x="338" y="237">tallow.flame.ni@hearthmail.example</text>
  <use href="#icon-globe" class="icon-paper" x="311" y="251" width="12" height="12"/>
  <text class="contact on-black" x="338" y="261">www.tallowflameni.example</text>
</svg>

<!-- Alternate card, centred brand -->
<svg class="card card--centered-black" viewBox="0 0 535 298" role="group" aria-label="Tallow Flame NI business card, centred black variant">
  <rect width="535" height="298" fill="var(--card-black)"/>
  <circle class="brand-dot" cx="135" cy="126" r="28"/>
  <text class="brand-name" x="135" y="190" text-anchor="middle">Tallow Flame NI</text>
  <text class="brand-tagline" x="135" y="200" text-anchor="middle">OIL BURNER SERVICING - MID ULSTER AREA</text>

  <line class="divider" x1="268" y1="42" x2="268" y2="256"/>

  <text class="person-name on-black" x="335" y="76">Owen Marsh</text>
  <text class="person-role on-black" x="336" y="97">Service Engineer</text>

  <use href="#icon-pin" class="icon-paper" x="308" y="160" width="12" height="12"/>
  <text class="contact on-black" x="335" y="171">#00 Adress 01, Adress, City</text>
  <use href="#icon-phone" class="icon-paper" x="308" y="185" width="12" height="12"/>
  <text class="contact on-black" x="335" y="196">077 51 364 927</text>
  <use href="#icon-at" class="icon-paper" x="308" y="211" width="12" height="12"/>
  <text class="contact contact--email on-black" x="335" y="222">tallow.flame.ni@hearthmail.example</text>
  <use href="#icon-globe" class="icon-paper" x="308" y="236" width="12" height="12"/>
  <text class="contact on-black" x="335" y="247">www.tallowflameni.example</text>
</svg>

</body>
</html>
```